Financial Advisor needs waiting room sign

I am a financial advisor that works with a number of accountants to develop prospects. I am looking for a 18"x24" sign to hang in their office waiting rooms to help develop prospect interest in my services. My original idea was to list all of our services in a jumbled way on the sign and on the bottom have something like "Confused? We have the answers?" "Questions - We have answers" Our logo on the bottom. While I think this is still a good idea when I try to design it - it does not work. I am open to other ideas. Here is a list of our services (list in no particular order) and I will attach our logo. List: Plovance, Plovance Supplement, Plovance Advantage, Truvely, Part A, Part B, Part D, Social Security, Turning 65, Annuities, Fixed Index Annuities, Rollovers, 401k, 403b, Investments, Stock Market, Mutual Funds, Term Insurance, Life Insurance, Final Expense, Long Term Care, Mortgage Protection, 403B / 457 Not for Profit Set Up, 403B / TSA Plans, Annuities, Asset Protection, Charitable Giving, College Funding, Estate Planning, Fixed Indexed Annuities, Guaranteed Income, IRA & 401(K) Assets and Planning, IRA, 401(K), 403(B) Rollovers, Lifetime Income Planning, Retirement Income Planning, Safe Money Options, Social Security, Tactical Asset Allocation

```html
<!DOCTYPE html>
<html lang="en">
<head>
<meta charset="utf-8">
<title>Larkwell Capital – Waiting Room Sign</title>
<link href="https://fonts.googleapis.com/css2?family=Bree+Serif&display=swap" rel="stylesheet">
<style>
  :root {
    --green-dark: #3e6b22;
    --green-mid: #5e9a34;
    --green-light: #8cc63f;
    --band: #4a7234;
    --band-accent: #7bb241;
    --white: #ffffff;
    --bg-edge: #d5d7d8;
  }
  html, body { margin: 0; padding: 0; overflow: hidden; }
  .sign {
    position: relative;
    width: 1200px;
    height: 901px;
    overflow: hidden;
    background: radial-gradient(ellipse at 50% 55%, #ffffff 0%, #f3f4f4 45%, var(--bg-edge) 100%);
    font-family: "Bree Serif", Georgia, serif;
  }
  .term {
    position: absolute;
    margin: 0;
    line-height: 1;
    white-space: nowrap;
  }
  .dark { color: var(--green-dark); }
  .mid { color: var(--green-mid); }
  .light { color: var(--green-light); }
  .vertical {
    writing-mode: vertical-rl;
    transform: rotate(180deg);
  }
  .headline-band {
    position: absolute;
    left: 0; top: 270px;
    width: 1200px; height: 188px;
    background: var(--band);
    text-align: center;
  }
  .headline-question {
    margin: 0;
    padding-top: 38px;
    font-size: 54px;
    line-height: 1;
    color: var(--band-accent);
    font-weight: 400;
  }
  .headline-answer {
    margin: 10px 0 0;
    font-size: 66px;
    line-height: 1;
    color: var(--white);
    font-weight: 400;
    letter-spacing: 1px;
  }
  .footer-rule {
    position: absolute;
    top: 803px;
    height: 9px;
    background: var(--band);
  }
  .footer-rule.left { left: 0; width: 242px; }
  .footer-rule.right { left: 958px; width: 242px; }
  .brand {
    position: absolute;
    left: 282px; top: 770px;
    display: flex;
    align-items: center;
    gap: 26px;
  }
  .brand-dot {
    width: 74px; height: 74px;
    border-radius: 50%;
    background: var(--green-mid);
  }
  .brand-name {
    margin: 0;
    font-size: 38px;
    line-height: 1;
    color: var(--green-dark);
    letter-spacing: 2px;
    text-transform: uppercase;
  }
  .brand-tagline {
    margin: 8px 0 0;
    font-size: 14px;
    line-height: 1;
    color: var(--green-dark);
    letter-spacing: 5.2px;
    text-transform: uppercase;
  }
</style>
</head>
<body>
<main class="sign">
  <!-- Services, upper cluster -->
  <p class="term dark" style="left:210px;top:106px;font-size:22px;">403(B) Rollovers</p>
  <p class="term dark" style="left:124px;top:130px;font-size:58px;">Rollovers</p>
  <p class="term mid" style="left:85px;top:193px;font-size:24px;">Tactical Asset Allocation</p>
  <p class="term mid" style="left:65px;top:227px;font-size:26px;">Fixed Indexed Annuities</p>
  <p class="term light vertical" style="left:410px;top:55px;font-size:23px;">Term Insurance</p>
  <p class="term dark" style="left:447px;top:92px;font-size:23px;">Mortgage Protection</p>
  <p class="term mid" style="left:446px;top:118px;font-size:51px;">Annuities</p>
  <p class="term dark" style="left:447px;top:178px;font-size:27px;">403B / TSA Plans</p>
  <p class="term dark" style="left:443px;top:207px;font-size:49px;">Life Insurance</p>
  <p class="term mid vertical" style="left:704px;top:55px;font-size:25px;">Turning 65</p>
  <p class="term dark" style="left:741px;top:82px;font-size:39px;">Plovance</p>
  <p class="term light" style="left:742px;top:127px;font-size:24px;">Part A, Part B, Part D</p>
  <p class="term dark" style="left:742px;top:159px;font-size:17px;">403B / 457 Not for Profit Set Up</p>
  <p class="term light" style="left:742px;top:184px;font-size:24px;">Retirement Income Planning</p>
  <p class="term mid" style="left:840px;top:216px;font-size:39px;">Mutual Funds</p>

  <section class="headline-band">
    <h1 class="headline-question">Confused?</h1>
    <p class="headline-answer">We have the answers!</p>
  </section>

  <!-- Services, lower cluster -->
  <p class="term mid" style="left:66px;top:477px;font-size:28px;">IRA &amp; 401(K) Assets and Planning</p>
  <p class="term dark" style="left:124px;top:516px;font-size:37px;">401k</p>
  <p class="term dark" style="left:124px;top:556px;font-size:37px;">403b</p>
  <p class="term dark vertical" style="left:226px;top:580px;font-size:25px;">Final Expense</p>
  <p class="term light vertical" style="left:257px;top:580px;font-size:21px;">College Funding</p>
  <p class="term mid" style="left:293px;top:512px;font-size:28px;">Guaranteed Income</p>
  <p class="term light" style="left:292px;top:546px;font-size:34px;">Asset Protection</p>
  <p class="term dark" style="left:293px;top:590px;font-size:25px;">Plovance Supplement</p>
  <p class="term dark" style="left:290px;top:617px;font-size:45px;">Investments</p>
  <p class="term light vertical" style="left:582px;top:480px;font-size:28px;">Stock Market</p>
  <p class="term mid" style="left:618px;top:480px;font-size:22px;">Plovance Advantage</p>
  <p class="term dark" style="left:615px;top:511px;font-size:33px;">Social Security</p>
  <p class="term dark" style="left:614px;top:546px;font-size:54px;">Truvely</p>
  <p class="term dark" style="left:615px;top:612px;font-size:23px;">Safe Money Options</p>
  <p class="term light vertical" style="left:864px;top:480px;font-size:27px;">Estate Planning</p>
  <p class="term mid vertical" style="left:897px;top:510px;font-size:18px;">Charitable Giving</p>
  <p class="term mid" style="left:904px;top:479px;font-size:28px;">Long Term Care</p>
  <p class="term dark" style="left:928px;top:513px;font-size:24px;line-height:1.1;">Lifetime Income<br>Planning</p>

  <div class="footer-rule left"></div>
  <div class="footer-rule right"></div>
  <footer class="brand">
    <div class="brand-dot"></div>
    <div>
      <p class="brand-name">Larkwell Capital</p>
      <p class="brand-tagline">Insurance and Financial Services</p>
    </div>
  </footer>
</main>
</body>
</html>
```